Consulting Firm Proposal Template

We need a template for proposals that we send to our clients using the attached outline. Our company is "Pennick Consulting Group". We would like a title page with the rest of the information on the following pages. The title page and subsequent pages should be designed in a way to support the use of pictures or graphics. We are looking to use a bold black and white color scheme. Overall we would like the design to confirm our deep experience and knowledge while still following modern design trends.

Target Market(s)

Medium Size Corporations

Industry/Entity Type

Consulting

Logo Text

Pennick Consulting Group

Font styles to use
Serif
Sans Serif

Colors

Designer to choose only greyscale colors for use in the design.

Requirements
Must have
• Title Page
Headers
Footers

```html
<!DOCTYPE html>
<html lang="en">
<head>
<meta charset="utf-8">
<title>Pennick Consulting Group – Business Proposal Folder</title>
<link href="https://fonts.googleapis.com/css2?family=Open+Sans:wght@400;600;700&display=swap" rel="stylesheet">
<style>
  :root {
    --stage: #d9d9d9;
    --ink: #1f1c1d;
    --paper: #ffffff;
    --text-dark: #222222;
    --text-mid: #4a4a4a;
    --text-light: #ffffff;
    --photo-top: #6b6a6e;
    --photo-mid: #b9bcc2;
    --photo-low: #4a4a50;
  }
  * { margin: 0; padding: 0; box-sizing: border-box; }
  html, body { width: 1200px; height: 783px; overflow: hidden; }
  body {
    background: var(--stage);
    font-family: "Open Sans", Arial, sans-serif;
    position: relative;
  }
  .folder {
    position: absolute;
    left: 80px; top: 41px;
    width: 1040px; height: 700px;
    display: flex;
    box-shadow: 0 8px 24px rgba(0,0,0,0.25);
  }
  .back-cover { width: 520px; height: 700px; background: var(--ink); }
  .front-cover {
    width: 520px; height: 700px;
    background: var(--paper);
    position: relative;
  }
  .cover-header {
    position: absolute; left: 0; top: 0;
    width: 100%; height: 112px;
    display: flex; align-items: center; justify-content: space-between;
    padding: 0 26px 0 26px;
  }
  .brand { display: flex; align-items: center; gap: 10px; }
  .brand-dot { width: 26px; height: 26px; border-radius: 50%; background: var(--text-dark); }
  .brand-name { font-size: 15px; font-weight: 700; color: var(--text-dark); }
  .contact-list { list-style: none; font-size: 8px; color: var(--text-mid); line-height: 1.3; }
  .contact-list li { display: flex; align-items: flex-start; gap: 8px; margin-bottom: 3px; }
  .contact-list li.address { margin-bottom: 9px; }
  .contact-list svg { width: 8px; height: 8px; flex: none; margin-top: 1px; }
  .cover-photo {
    position: absolute; left: 0; top: 112px;
    width: 100%; height: 218px;
    background: linear-gradient(180deg, var(--photo-top) 0%, var(--photo-mid) 40%, var(--photo-mid) 60%, var(--photo-low) 100%);
  }
  .title-band {
    position: absolute; left: 0; top: 330px;
    width: 100%; height: 248px;
    background: var(--ink);
    color: var(--text-light);
  }
  .cover-title {
    position: absolute; left: 34px; top: 42px;
    font-size: 50px; font-weight: 700; letter-spacing: 0.5px;
  }
  .prepared-for {
    position: absolute; left: 48px; top: 138px;
    font-size: 11px; line-height: 1.45;
  }
</style>
</head>
<body>
  <div class="folder">
    <div class="back-cover"></div>
    <section class="front-cover">
      <header class="cover-header">
        <div class="brand">
          <span class="brand-dot"></span>
          <span class="brand-name">Pennick Consulting Group</span>
        </div>
        <ul class="contact-list">
          <li class="address">
            <svg viewBox="0 0 10 10"><path d="M5 0.5a3.3 3.3 0 0 0-3.3 3.3C1.7 6.3 5 9.5 5 9.5s3.3-3.2 3.3-5.7A3.3 3.3 0 0 0 5 0.5z" fill="none" stroke="#555" stroke-width="0.9"/><circle cx="5" cy="3.8" r="1.1" fill="#555"/></svg>
            <span>14 Alder Lane, Rondebosch, Cape Town,<br>7701, South Africa</span>
          </li>
          <li>
            <svg viewBox="0 0 10 10"><path d="M2 1l2 2-1 1.2c.6 1.2 1.6 2.2 2.8 2.8L7 6l2 2-1.3 1.3C4.5 9 1 5.5.7 2.3z" fill="#222"/></svg>
            <span>+27 21 555 0148</span>
          </li>
          <li>
            <svg viewBox="0 0 10 10"><rect x="0.5" y="2" width="9" height="6" fill="#222"/><path d="M0.5 2l4.5 3.5L9.5 2" fill="none" stroke="#fff" stroke-width="0.8"/></svg>
            <span>info@pennick.co.za</span>
          </li>
          <li>
            <svg viewBox="0 0 10 10"><circle cx="5" cy="5" r="4.3" fill="none" stroke="#333" stroke-width="0.8"/><ellipse cx="5" cy="5" rx="1.8" ry="4.3" fill="none" stroke="#333" stroke-width="0.7"/><path d="M0.7 5h8.6" stroke="#333" stroke-width="0.7"/></svg>
            <span>www.pennick.co.za</span>
          </li>
        </ul>
      </header>
      <div class="cover-photo" role="img" aria-label="Photograph of a business team meeting around a table in a glass-walled office"></div>
      <div class="title-band">
        <h1 class="cover-title">Business Proposal</h1>
        <p class="prepared-for">Prepared for:<br>Daniel Reed</p>
      </div>
    </section>
  </div>
</body>
</html>
```